Designing a new homepage for www.Brindlework.net

WEBSITE: www.brindlework.net

ABOUT THE WEBSITE
The Brindlework.net (BWK) website contains a large directory of over 50,000 international trade service providers that is not valued enough on the homepage (HP). Currently from the HP, the site appears as a general site about imports and exports (international trade). As a result, it contradicts the purpose and experience of the site.
The website is new and original for international trade online: it is a tool to find the best experts and professionals that can help importers and exporters to implement their overseas operations.

Specifically:
a) An exporter who wants to sell in Italy can find on BWK: agents to distribute their products, a lawyer for reviewing contracts, translators to translate brochures and websites, an export consultant, etc. Various local providers that can help sell their products in Italy, a local provider (e.g. based in Italy) are generally more efficient and less costly than a supplier in the exporter’s home country

b) An importer who wants to buy in China will find purchasing agents who source products for third parties; logistics companies that store and ship merchandise; corporate quality control to ensure product quality before shipment, etc.; various local providers based in China to better organize its import operation.

BWK is therefore a very resourceful solution for SMEs who want to develop, improve and organize their international trade:
a) it significantly increases their ability to create new opportunities by using the services of a third party: export to a new country; import a new product
b) it allows them to optimize their purchases of services by seeking alternatives: find a less expensive carrier, a foreign lawyer challenged by a local lawyer

It is the perfect complement to cross border marketplaces (e.g. Quorvanta.com, fenwickmarts.com, zl48.com) which concentrate on the search for products (and of companies/counterparts) but:
a) help the user to import only, not really export
b) do not help implement the operations of exporting/importing from A to Z

Therefore, BWK offers a new way of “easy exporting” (or easy importing).

THE BRIEF

The objective of the project is to rethink the HP (and the site design) to highlight this experience: "export and import more successfully through 50,000+ service providers in over 100 countries”.
We have created a wireframe (see attached) of the structure we feel best meets this objective. What do you think? Do we meet it through our wireframe? Then, next step is to take this wireframe and create a clear design that really helps us to achieve our objective.

It is considered that the site captures the importers/exporters seeking to increase their exports or to better organize their imports (but we do not start from a priori that these users are looking for service providers).
The HP should highlight the importance of service providers addressing export markets or better organizing their imports; the "market analyses" of the site should act as a "knowledge resource", where the site offers more the main experience: if you want to export to a country you have any interest to first explore what the partners listed by BWK can provide.

Reason: We feel that we're seeing some interesting designs and would like to give current and even potential submissions more time. So far we have not seen the one that really strikes us, so perhaps more time is what we and the designers need! Thanks!

Target Market(s)

Importers, exporters, international trade service providers, foreign investors, etc

Industry/Entity Type

Lawyer

Requirements
Must have
• • Please use the current basic design elements of the website, including the logo, (www.brindlework.net). These include colors and fonts, etc. We only aim to change the HP and therefore, only implement a change to the header and footer of the whole site.
• Please find inspiration from our wireframes (attached), as they have been carefully thought about by our own team. However, should you feel the need to challenge the wireframes, please do so in your design, we're interested to see what you can present us.
• Our prime objective in terms of design: creating a more user-friendly interface on the HP to guide users into the rest of the website
• We already have a psd file based on the wireframes we’ve attached to the brief. If you would like this, so your job is easier (such as using same text as we have in the wireframes), let us know!

```html
<!DOCTYPE html>
<html lang="en">
<head>
<meta charset="utf-8">
<title>Brindlework.net – International Trade Service Providers</title>
<link href="https://fonts.googleapis.com/css2?family=Open+Sans:wght@300;400;600;700&display=swap" rel="stylesheet">
<style>
:root{
  --page:#eeeeee;
  --white:#ffffff;
  --ink:#333333;
  --muted:#777777;
  --soft:#999999;
  --line:#dcdcdc;
  --heading:#2c4a66;
  --blue:#1e7fc7;
  --blue-dark:#155f97;
  --blue-deep:#0f4775;
  --link:#1e6fb0;
  --panel:#e6e6e6;
  --footer:#e3e3e3;
  --bottom:#7a7a7a;
  --star:#f0a81c;
  --red:#c9302c;
}
*{box-sizing:border-box;margin:0;padding:0}
html,body{width:1200px;height:2500px;overflow:hidden}
body{background:var(--page);font-family:"Open Sans",Arial,sans-serif;color:var(--ink);font-size:13px;position:relative}
a{color:var(--link);text-decoration:none}
ul{list-style:none}
.abs{position:absolute}

/* top bar */
.topbar{left:0;top:0;width:1200px;height:42px;background:#f4f4f4;border-bottom:1px solid var(--line)}
.topnav{left:119px;top:12px;display:flex;gap:22px;font-size:11px;color:var(--muted)}
.topnav .current{color:var(--ink);text-decoration:underline}
.like{display:flex;align-items:center;gap:5px}
.like i{width:11px;height:11px;background:var(--link);display:inline-block}
.account{right:119px;top:6px;display:flex;gap:8px}
.account span{display:inline-block;padding:6px 16px;font-size:11px;border:1px solid #cfcfcf;background:linear-gradient(#fff,#ececec);color:var(--ink);border-radius:2px}
.account span:last-child{padding:6px 22px}

/* header */
.header{left:0;top:42px;width:1200px;height:96px;background:var(--white)}
.logo{left:119px;top:28px;display:flex;align-items:center;gap:10px;font-size:26px;font-weight:300;letter-spacing:5px;color:var(--heading)}
.logo i{width:20px;height:20px;border-radius:50%;background:var(--heading);display:inline-block}
.ad{left:610px;top:14px;width:474px;height:50px;background:#3a93d8;display:flex;align-items:center}
.ad b{color:#fff;font-weight:700;font-size:16px;padding-left:12px;flex:1;white-space:nowrap}
.ad div{width:130px;height:50px;background:linear-gradient(135deg,#e9dcc4,#c9a878)}

/* main shell */
.shell{left:69px;top:137px;width:1062px}
.tabs{height:63px;background:linear-gradient(#ececec,#dedede);border:1px solid #d0d0d0;display:flex;align-items:center;padding-left:50px;gap:30px;font-size:13px;color:var(--muted);text-transform:uppercase}
.tabs .active{background:var(--blue);color:#fff;padding:10px 20px;border-radius:2px}
.search{margin-left:auto;margin-right:24px;display:flex}
.search span{width:330px;height:38px;border:1px solid #ccc;background:#fff;font-size:12px;color:var(--soft);display:flex;align-items:center;padding-left:12px;text-transform:none}
.search i{width:44px;height:38px;background:var(--blue);display:flex;align-items:center;justify-content:center}

.hero{height:270px;background:var(--white);position:relative;border-left:1px solid #ddd;border-right:1px solid #ddd}
.hero h1{position:absolute;left:50px;top:36px;font-weight:300;font-size:32px;color:var(--heading);z-index:2;white-space:nowrap}
.hero h2{position:absolute;left:50px;top:104px;font-size:17px;font-weight:700;line-height:1.3;color:var(--ink)}
.hero ul{position:absolute;left:50px;top:160px;font-size:15px;color:var(--muted);line-height:27px}
.hero ul li::before{content:"•";margin-right:8px}
.hero-photo{position:absolute;left:600px;top:0;width:430px;height:270px;background:linear-gradient(135deg,#d9dde2,#8a8f97 55%,#3d3f44)}
.listed{position:absolute;left:900px;top:196px;display:flex;align-items:flex-end;gap:6px;font-size:10px;color:#eee;line-height:1.2;width:150px;z-index:2}
.listed i{width:36px;height:36px;background:#bdbdbd;flex:none}

.startbar{height:88px;background:linear-gradient(#3394dc,#1b75bb);display:flex;align-items:center;padding-left:50px;color:#fff;box-shadow:0 8px 10px -6px rgba(0,0,0,.35)}
.startbar strong{font-size:22px;font-weight:700;margin-right:22px}
.select{width:277px;height:46px;background:#fff;color:var(--muted);font-size:12px;display:flex;align-items:center;justify-content:space-between;padding-left:14px;border-radius:2px}
.select i{width:42px;height:46px;border-left:1px solid #ddd;display:flex;align-items:center;justify-content:center}
.startbar .assist{margin:0 12px 0 24px;font-size:15px}
.check{display:flex;align-items:center;gap:8px;font-size:15px;margin-right:22px}
.check i{width:17px;height:17px;background:#fff;border:1px solid #9cc8ea;display:flex;align-items:center;justify-content:center}
.go{margin-left:34px;width:70px;height:56px;background:var(--blue-deep);font-size:23px;font-weight:600;display:flex;align-items:center;justify-content:center;border-radius:2px}

/* export panel */
.export{left:69px;top:608px;width:1062px;height:284px;background:var(--panel);border:1px solid #d2d2d2}
.export h3{position:absolute;left:50px;top:26px;font-size:31px;font-weight:300;color:var(--heading)}
.export .sub{position:absolute;left:50px;top:66px;font-size:16px;color:var(--muted)}
.countries{position:absolute;right:30px;top:34px;display:flex;gap:50px;font-size:17px;color:var(--soft)}
.featured{position:absolute;left:50px;top:110px;display:flex;gap:14px;width:420px}
.seal{width:76px;height:76px;border-radius:50%;background:#c7c7c7;flex:none}
.featured h4{font-size:17px;font-weight:400;color:var(--ink)}
.featured .kind{font-size:14px;color:var(--muted)}
.featured p{font-size:11px;color:var(--soft);line-height:1.5;margin-top:10px}
.featured-links{position:absolute;left:140px;top:232px;width:330px;display:flex;justify-content:space-between;font-size:12px;color:var(--muted)}
.featured-links a{text-decoration:underline;color:var(--ink)}
.divider{position:absolute;left:478px;top:110px;width:1px;height:145px;background:#c6c6c6}
.stat{position:absolute;top:110px}
.stat b{display:block;font-size:38px;font-weight:300;color:var(--heading);line-height:1.1}
.stat span{display:block;font-size:16px;color:var(--ink);line-height:1.2;margin-top:8px}
.stat em{display:block;font-style:normal;font-size:13px;color:var(--muted)}
.stat a{display:block;margin-top:10px;font-size:11px;color:var(--ink)}

/* columns */
.col{top:927px}
.col h5,.tips h5,.knowledge h5{font-size:16px;font-weight:400;color:var(--heading);padding-bottom:12px;border-bottom:1px solid var(--line)}
.dir{left:119px;width:298px}
.toggle{display:flex;margin:16px 0 14px}
.toggle span{flex:1;height:38px;display:flex;align-items:center;justify-content:center;font-size:13px;background:linear-gradient(#f4f4f4,#dcdcdc);color:var(--muted);border:1px solid #ccc}
.toggle .on{background:var(--blue);color:#fff;border-color:var(--blue)}
.dir li{font-size:12.5px;color:var(--ink);line-height:25.3px}
.dir li::before{content:"•";margin-right:6px}
.dir li small{color:var(--soft);font-size:12px}
.dir li.sub{padding-left:14px}
.dir li.sub a{color:var(--link);font-weight:700;text-decoration:underline}

.say{left:448px;width:302px}
.quote{position:relative;padding:16px 0 14px;border-bottom:1px solid var(--line)}
.quote .who{display:flex;gap:16px}
.avatar{width:58px;height:58px;background:linear-gradient(#c9ced6,#7c8794);flex:none;border:2px solid #fff;box-shadow:0 0 0 1px #ddd}
.who a{font-size:15px;color:var(--link)}
.who b{display:block;font-size:17px;font-weight:400;color:var(--ink);line-height:1.2}
.who span{font-size:13px;color:var(--muted)}
.quote p{margin-top:12px;font-size:11.5px;font-style:italic;line-height:1.5;color:var(--ink);width:262px;position:relative;z-index:1}
.mark{position:absolute;right:0;top:60px;font-size:150px;color:#e7e7e7;font-family:Georgia,serif;line-height:1}
.qfoot{display:flex;justify-content:space-between;align-items:center;margin-top:12px;font-size:12px;min-height:26px}
.qfoot a{text-decoration:underline;color:var(--ink)}
.btn{border:1px solid #ccc;background:linear-gradient(#fff,#ececec);padding:6px 14px;font-size:11px;border-radius:2px;color:var(--ink)}

.providers{left:777px;width:354px}
.prov{display:flex;gap:18px;padding:16px 0 14px;border-bottom:1px solid var(--line)}
.brand{width:70px;display:flex;flex-direction:column;align-items:center;gap:6px;font-size:11px;font-weight:600;color:var(--ink);flex:none;padding-top:4px}
.brand i{width:34px;height:34px;background:#555;display:block}
.prov h6{font-size:15px;font-weight:600;color:var(--link)}
.prov em{display:block;font-style:normal;font-size:12px;font-weight:600;color:var(--ink);margin-bottom:6px}
.prov p{font-size:12px;color:var(--ink);line-height:1.45}
.prov a{display:block;margin-top:6px;font-size:11px;color:var(--muted)}
.free{margin-top:18px;height:118px;background:linear-gradient(#3394dc,#1b75bb);color:#fff;padding:16px 22px}
.free b{font-size:19px;font-weight:400;line-height:1.25;display:block}
.free b strong{font-weight:700}
.free div{display:flex;justify-content:space-between;align-items:center;margin-top:16px;font-size:11px}
.free .btn{color:var(--ink)}

.tips{left:448px;top:1552px;width:302px}
.tip{padding:22px 0 14px;border-bottom:1px solid var(--line)}
.tip b{font-size:14px;font-weight:400;color:var(--ink)}
.tip p{font-size:12px;color:var(--muted);line-height:1.4}
.rate{display:flex;justify-content:flex-end;align-items:center;gap:6px;font-size:11px;color:var(--muted);margin-top:6px}
.stars{color:var(--star);letter-spacing:1px;font-size:13px}
.stars em{color:#ccc;font-style:normal}
.pdf{width:14px;height:16px;background:var(--red)}
.tipsfoot{display:flex;justify-content:space-between;align-items:center;margin-top:18px;font-size:11px;color:var(--muted)}

.knowledge{left:777px;top:1552px;width:354px}
.knowledge .lead{font-size:14px;font-weight:600;margin:26px 0 10px}
.knowledge ul li{font-size:14px;line-height:24px;color:var(--ink)}
.knowledge ul li::before{content:"•";margin-right:8px;color:var(--muted)}
.knowledge ul li b{font-weight:400;color:var(--link);display:inline-block;width:70px}
.kselect{display:flex;gap:10px;margin:18px 0 20px}
.kselect .select{width:242px;height:40px;border:1px solid #ccc;background:linear-gradient(#fff,#eee)}
.kselect .select i{height:38px}
.ok{width:56px;height:40px;background:var(--blue);color:#fff;font-weight:600;display:flex;align-items:center;justify-content:center;border-radius:2px}
.popular b{font-size:13px;font-weight:600}
.popular p{font-size:12.5px;line-height:1.65;color:var(--ink);margin-top:6px}
.popular p u{color:var(--link);font-weight:600}

/* partners */
.partners{left:0;top:2070px;width:1200px;height:128px;border-top:1px solid var(--line);display:flex;align-items:center;justify-content:center;gap:52px}
.partners i{display:block;background:#b4b4b4}

/* footer */
.footer{left:0;top:2198px;width:1200px;height:260px;background:var(--footer);border-top:1px solid #d0d0d0}
.fcol{position:absolute;top:22px;width:200px}
.fcol h6{font-size:14px;font-weight:600;color:var(--link);margin-bottom:10px}
.fcol li{font-size:11.5px;line-height:22px;color:var(--muted)}
.fcol li.strong{font-weight:700;color:var(--ink)}
.fcol li.u{text-decoration:underline;color:var(--ink)}
.follow{left:889px;top:2194px;width:190px;height:264px;background:linear-gradient(#2e8fd8,#176eb1);color:#fff;padding:20px 28px}
.follow h6{font-size:14px;font-weight:600;margin-bottom:12px}
.follow li{display:flex;align-items:center;gap:10px;font-size:12px;line-height:22px}
.follow li i{width:12px;height:12px;background:#fff;display:block}
.follow h6.join{margin-top:20px}
.bottom{left:0;top:2458px;width:1200px;height:42px;background:var(--bottom);color:#f1f1f1;font-size:11px;display:flex;align-items:center;justify-content:center}
</style>
</head>
<body>

<div class="abs topbar">
  <nav class="abs topnav"><span class="current">Home</span><span>About us</span><span>Take a tour</span><span>Advertise</span><span>Why Brindlework.net?</span><span class="like"><i></i>Like</span></nav>
  <div class="abs account"><span>Login</span><span>Sign Up</span><span>List Your Services</span></div>
</div>

<header class="abs header">
  <div class="abs logo"><i></i>BRINDLEWORK.net</div>
  <div class="abs ad"><b>Peanuts! Peanuts! Who wants peanuts?</b><div role="img" aria-label="Advert photo of peanuts"></div></div>
</header>

<main class="abs shell">
  <div class="tabs">
    <span>All trade services</span><span>Let us help you</span><span class="active">Browse knowledge</span>
    <div class="search"><span>Search 20,000+ content items &amp; 50,000+ services…</span><i><svg width="18" height="18" viewBox="0 0 18 18"><circle cx="7.5" cy="7.5" r="5.5" fill="none" stroke="#fff" stroke-width="2"/><line x1="11.5" y1="11.5" x2="16" y2="16" stroke="#fff" stroke-width="2.5"/></svg></i></div>
  </div>
  <section class="hero">
    <div class="hero-photo" role="img" aria-label="Photo of two business people working at a laptop"></div>
    <h1>Improve Your business overseas!</h1>
    <h2>Use the leverage of 51,000+<br>verified services providers:</h2>
    <ul><li>Sales agents, market entry, customs services</li><li>Sourcing companies, freight forwarders, quality control</li><li>Lawyers, accounting, expat services and more</li></ul>
    <div class="listed">Includes the service providers listed by:<i></i></div>
  </section>
  <div class="startbar">
    <strong>Start now:</strong>
    <div class="select">Select your target country<i><svg width="12" height="8" viewBox="0 0 12 8"><path d="M1 1l5 5 5-5" fill="none" stroke="#888" stroke-width="2"/></svg></i></div>
    <span class="assist">and find assistance to</span>
    <span class="check"><i></i>Import</span>
    <span class="check"><i><svg width="11" height="11" viewBox="0 0 11 11"><path d="M1 1l9 9M10 1l-9 9" stroke="#333" stroke-width="2"/></svg></i>Export</span>
    <span class="check"><i></i>Invest</span>
    <span class="go">GO</span>
  </div>
</main>

<section class="abs export">
  <h3>Want to export to South Africa?</h3>
  <p class="sub">Discover 451 Service Providers to help you export including:</p>
  <div class="countries"><span>« Brazil</span><span>China »</span></div>
  <div class="featured">
    <div class="seal"></div>
    <div><h4>Kestrelgate South Africa</h4><div class="kind">Export support</div>
    <p>Sed nibh sapien, elementum dignissim eleifend nec, adipiscing sit amet lectus. Donec quis tortor eros, ut egestas metus. Nunc posuere molestie ultrices.</p></div>
  </div>
  <div class="featured-links"><a>www.kestrelgate.com</a><span>Want your logo here?</span></div>
  <div class="divider"></div>
  <div class="stat" style="left:520px"><b>25</b><span>Freight<br>Forwarders</span><em>in South Africa</em><a>See all</a></div>
  <div class="stat" style="left:697px"><b>47</b><span>Corporate<br>Lawyers</span><em>in South Africa</em><a>See all</a></div>
  <div class="stat" style="left:857px"><b>56</b><span>Debt<br>Collectors</span><em>in South Africa</em><a>See all</a></div>
</section>

<section class="abs col dir">
  <h5>Browse our directory</h5>
  <div class="toggle"><span class="on">Services 200+</span><span>Countries 100+</span></div>
  <ul>
    <li>Freight Forwarders <small>(7843)</small></li><li>Trading Companies <small>(2489)</small></li><li>Corporate Law <small>(975)</small></li>
    <li class="sub"><a>Investment Promotion (817)</a></li>
    <li>Distributors <small>(656)</small></li><li>Tranlation <small>(621)</small></li><li>Debt Collection <small>(561)</small></li><li>Accounting Services <small>(519)</small></li><li>Expat Services <small>(512)</small></li><li>Market Research <small>(512)</small></li><li>Debt Collection <small>(561)</small></li>
    <li>Freight Forwarders <small>(7843)</small></li><li>Trading Companies <small>(2489)</small></li><li>Corporate Law <small>(975)</small></li><li>Investment Promotion <small>(817)</small></li><li>Distributors <small>(656)</small></li><li>Tranlation <small>(621)</small></li><li>Debt Collection <small>(561)</small></li><li>Accounting Services <small>(519)</small></li><li>Expat Services <small>(512)</small></li><li>Market Research <small>(512)</small></li><li>Debt Collection <small>(561)</small></li>
    <li>Freight Forwarders <small>(7843)</small></li><li>Trading Companies <small>(2489)</small></li><li>Corporate Law <small>(975)</small></li><li>Investment Promotion <small>(817)</small></li><li>Distributors <small>(656)</small></li><li>Tranlation <small>(621)</small></li><li>Expat Services <small>(512)</small></li><li>Market Research <small>(512)</small></li><li>Debt Collection <small>(561)</small></li>
    <li>Freight Forwarders <small>(7843)</small></li><li>Trading Companies <small>(2489)</small></li><li>Corporate Law <small>(975)</small></li><li>Investment Promotion <small>(817)</small></li><li>Distributors <small>(656)</small></li><li>Tranlation <small>(621)</small></li>
  </ul>
</section>

<section class="abs col say">
  <h5>What Importers / Exporters say</h5>
  <div class="quote">
    <div class="who"><div class="avatar" role="img" aria-label="Portrait photo of the speaker"></div><div><a>Name Of Speaker</a><b>Sourcing Services</b><span>Florida, The United States</span></div></div>
    <span class="mark">“</span>
    <p>"Sed nibh sapien, elementum dignissim eleifend nec, adipiscing sit amet lectus. Donec quis tortor eros, ut egestas metus. Nunc posuere molestie ultrices. Morbi at dui diam commodo venenatis eu in felis. Nam quis tellus non nibh lobortis placerat. Nam tristique metus in odio vehicula convallis. Donec condimentum elementum dui nec faucibus."</p>
    <div class="qfoot"><a>See the benefits</a></div>
  </div>
  <div class="quote">
    <div class="who"><div class="avatar" role="img" aria-label="Portrait photo of the speaker"></div><div><a>Name Of Speaker</a><b>Investment Promotion</b><span>Dhaka, India</span></div></div>
    <span class="mark">“</span>
    <p>"Ut posuere porta aliquet. Fusce sollicitudin imperdiet odio, a semper est feugiat blandit. Morbi eros lorem, cursus non sollicitudin rutrum, sagittis et lacus. Nam eget purus arcu, id posuere dolor. Donec facilisis purus quis libero malesuada vitae tempus elit condimentum."</p>
    <div class="qfoot"><a>See the benefits</a><span class="btn">Join for FREE</span></div>
  </div>
</section>

<section class="abs col providers">
  <h5>New Service Providers</h5>
  <div class="prov"><div class="brand"><i></i>Corvane</div><div><h6>Corvane Media Limited</h6><em>Tax Services in the United Kingdom</em><p>Lorem ipsum dolor sit amet, consectetur adipiscing elit. Suspendisse auctor quam sed magna ultricies rhoncus.</p><a>View Profile</a></div></div>
  <div class="prov"><div class="brand"><i></i>Larchmont</div><div><h6>Larchmont Trade Financing</h6><em>Factoring in the United States</em><p>Lorem ipsum dolor sit amet, quisque a vestibulum dolor posuere non.</p><a>View Profile</a></div></div>
  <div class="prov"><div class="brand"><i></i>EBMF</div><div><h6>Eastholm Building Materials Fed.</h6><em>Professional Associacion in China</em><p>Cum sociis natoque penatibus et magnis dis parturient montes, nascetur ridiculus mus.</p><a>View Profile</a></div></div>
  <div class="free"><b>It's <strong>FREE to list</strong> your services on <strong>brindlework.net</strong></b><div><span>See the benefits</span><span class="btn">List Your Services</span></div></div>
</section>

<section class="abs tips">
  <h5>Business Tips By Experts</h5>
  <div class="tip"><b>Business administration</b><p>Nullam massa metus, eleifend nec tincidunt vel, scelerisque vel urna.</p><div class="rate"><span class="stars">★★★<em>★★</em></span>Rated<span class="pdf"></span></div></div>
  <div class="tip"><b>Business administration</b><p>Nullam massa metus, eleifend nec tincidunt vel, scelerisque vel urna.</p><div class="rate"><span class="stars">★★★<em>★★</em></span>Rated<span class="pdf"></span></div></div>
  <div class="tip"><b>Business administration</b><p>Nullam massa metus, eleifend nec tincidunt vel, scelerisque vel urna.</p><div class="rate"><span class="stars">★★★<em>★★</em></span>Rated<span class="pdf"></span></div></div>
  <div class="tipsfoot"><span>Browse all content</span><span class="btn">Receive Updates</span></div>
</section>

<section class="abs knowledge">
  <h5>Knowledge Resource</h5>
  <p class="lead">Find resources for your business amongst:</p>
  <ul><li><b>10,145</b>Market analyses</li><li><b>9,254</b>Business tips</li><li><b>3,215</b>Agents and distributors</li><li><b>50,145</b>Service providers</li></ul>
  <div class="kselect"><div class="select">Select a Country<i><svg width="12" height="8" viewBox="0 0 12 8"><path d="M1 1l5 5 5-5" fill="none" stroke="#888" stroke-width="2"/></svg></i></div><span class="ok">OK</span></div>
  <div class="popular"><b>Most popular:</b><p>China, Brazil, Japan, India, Egypt, Korea, Angola, Italy, England, Romania, <u>Spain</u>, Argentina, France, China, Brazil, Japan, India, Egypt, Korea, Angola, Africa, United States, Thailand, Singapore, Hungary, Germany, Russia, China, Vietnam, France</p></div>
</section>

<div class="abs partners">
  <i style="width:64px;height:64px"></i><i style="width:66px;height:56px"></i><i style="width:160px;height:36px"></i><i style="width:110px;height:42px"></i><i style="width:146px;height:36px"></i><i style="width:150px;height:70px"></i>
</div>

<footer class="abs footer">
  <div class="fcol" style="left:129px"><h6>About</h6><ul><li>About us</li><li>Partners</li><li>Site Map</li><li>Contact Us</li><li>Terms &amp; Conditions</li><li>Privacy Policy</li></ul></div>
  <div class="fcol" style="left:279px"><h6>Most Popular Pages</h6><ul><li>Distributors</li><li>Country Risk</li><li>Tax Law</li><li>Market Research</li><li>Business Development</li><li>Mergers and Acquisitions</li><li>Corporate Law</li><li>View all</li></ul></div>
  <div class="fcol" style="left:469px"><h6>For Importers / Exporters</h6><ul><li>Import Export Services</li><li>Trade Companies, Agents</li><li>Market Analyses Worldwide</li><li class="strong">International Business Tips</li><li>Receive Offers for Services</li><li>Take a tour</li></ul></div>
  <div class="fcol" style="left:690px"><h6>For Service Providers</h6><ul><li>Import Export Services</li><li>Trade Companies, Agents</li><li>Market Analyses Worldwide</li><li>International Business Tips</li><li>Receive Offers for Services</li><li class="u">Take a tour</li></ul></div>
</footer>
<aside class="abs follow">
  <h6>Follow Us</h6>
  <ul><li><i></i>Newsletter</li><li><i></i>Flitline</li><li><i></i>RSS</li></ul>
  <h6 class="join">Join Us</h6>
  <ul><li><i></i>Circleroom</li><li><i></i>Workchain</li></ul>
</aside>
<div class="abs bottom">Brindlework.net - International Trade Resources, Import Export Services © 2012. All Rights Reserved.</div>

</body>
</html>
```